MBRCCUL re-branding website and logo

We are looking for a new webpage design and logo our current page address is www.mbrccul-example.org. We want to create a new design using MBRCCUL Mariners and Bakers Regional Co-operative Credit Union limited and another with the purposed new name MBFC Mariners and Bakers Financial Co-operative, the color scheme is purple and burnt orange. Our new logo and webpage should communicate change and growth purposed theme continuing our legacy here to server past, present and future generations. Our idea for the logo is a live shot of hands of different ages in a circle holding a tree

Target Market(s)

Everyone

Contact Information for Business Card

Company Name
Telephone number
Address
slot to enter employee info

Logo Text

(M & B) Mariners And Bakers Financial Co-operative

Coding

Coded - Design and coding required

Number of Pages Required

2 page

Colors
f37122
fbed22
6b449b

Requirements
Must have
• links for social media

```html
<!DOCTYPE html>
<html lang="en">
<head>
<meta charset="utf-8">
<title>Mariners and Bakers Financial Co-operative</title>
<link href="https://fonts.googleapis.com/css2?family=Lato:wght@300;400;700;900&display=swap" rel="stylesheet">
<style>
:root{
  --orange:#f37122;
  --purple:#6b449b;
  --black:#000;
  --ink:#222;
  --muted:#666;
  --soft-pink:#efe3e3;
  --card:#f6f4f4;
  --footer-nav:#3b3b3b;
  --footer:#2d2d2d;
  --white:#fff;
}
*{box-sizing:border-box;margin:0;padding:0}
html,body{width:1200px;height:2795px;overflow:hidden}
body{font-family:'Lato',sans-serif;color:var(--ink);background:var(--white);position:relative}
a{color:inherit;text-decoration:none}

/* header */
.site-header{position:absolute;left:0;top:0;width:1200px;height:112px;background:var(--black);color:var(--white)}
.brand{position:absolute;left:86px;top:38px}
.brand-name{font-size:24px;font-weight:400;letter-spacing:.5px;color:var(--white)}
.utility-nav{position:absolute;right:86px;top:18px;display:flex;gap:18px;font-size:12.5px;align-items:center}
.utility-nav .tel{display:flex;align-items:center;gap:5px}
.main-nav{position:absolute;left:454px;top:57px;display:flex;gap:16px;font-size:15px}
.login-btn{position:absolute;left:902px;top:47px;width:210px;height:42px;border:1px solid #555;background:#222;font-size:12.5px;display:flex;align-items:center;justify-content:center;gap:20px;text-transform:uppercase}

/* hero */
.hero{position:absolute;left:0;top:112px;width:1200px;height:454px}
.hero-photo{position:absolute;inset:0;background:linear-gradient(90deg,#eeece9 0%,#e6e2dc 40%,#cdbba7 60%,#e9e3db 80%,#f1efec 100%)}
.hero-photo::after{content:"";position:absolute;left:0;right:0;bottom:0;height:90px;background:linear-gradient(180deg,rgba(190,175,160,0),#b8a894)}
.hero-title{position:absolute;left:86px;top:140px;font-size:34px;font-weight:700;color:var(--orange)}
.hero-copy{position:absolute;left:86px;top:188px;width:440px;font-size:12.5px;line-height:23px;color:#555}
.btn{display:inline-flex;align-items:center;justify-content:center;color:var(--white);font-weight:700}
.btn-purple{background:var(--purple)}
.hero .btn{position:absolute;left:86px;top:274px;width:128px;height:35px;font-size:16px}
.dots{position:absolute;left:86px;top:339px;display:flex;gap:8px}
.dots i{width:10px;height:10px;border-radius:50%;background:#fff;display:block}
.dots i.on{background:var(--orange)}

/* services */
.section-title{position:absolute;left:0;width:1200px;text-align:center;font-size:27px;font-weight:400}
.service{position:absolute;top:747px;width:200px;text-align:center;font-size:15px;line-height:19px;color:#444}
.service .ring{width:127px;height:127px;border-radius:50%;background:var(--soft-pink);margin:0 auto 20px;display:flex;align-items:center;justify-content:center}
.service .ring.active{background:var(--orange);border:3px solid var(--orange);outline:4px solid #fff;outline-offset:-8px}

/* rates */
.rates{position:absolute;left:0;top:984px;width:1200px;height:493px;background:var(--black);color:var(--white)}
.rates .section-title{top:58px;color:var(--white)}
.rate-card{position:absolute;top:124px;width:201px;height:233px;border:1px solid #555;text-align:center}
.rate-card svg{margin-top:30px}
.rate-name{font-size:15.5px;margin-top:14px}
.rate-sub{font-size:10px;color:#ccc;margin-top:2px}
.rate-value{display:inline-block;background:var(--orange);font-size:16px;padding:10px 14px;margin-top:12px}
.rates-note{position:absolute;left:0;width:1200px;top:396px;display:flex;justify-content:center;align-items:center;gap:14px;font-size:17px}
.rates-note .btn{width:170px;height:35px;font-size:15px;font-weight:400}

/* news */
.news-card{position:absolute;top:1600px;width:332px;height:509px;background:var(--card)}
.news-photo{height:319px}
.news-body{padding:28px 16px 0}
.news-title{font-size:14.5px;font-weight:700;color:#222}
.news-text{font-size:11.5px;line-height:21px;color:#555;margin-top:12px}
.news-meta{font-size:11px;color:#777;margin-top:14px;display:flex;gap:22px;align-items:center}
.news-meta span{display:flex;gap:5px;align-items:center}

/* notice */
.notice{position:absolute;left:0;top:2148px;width:1200px;height:367px;background:linear-gradient(90deg,#4a4a48 0%,#5a5854 45%,#7d776c 70%,#6a6864 100%);color:var(--white)}
.notice-title{position:absolute;left:86px;top:82px;font-size:31px;font-weight:700;letter-spacing:.5px}
.notice-copy{position:absolute;left:86px;top:148px;font-size:15.5px;line-height:30px}
.notice-copy strong{font-size:20px;letter-spacing:.3px}
.notice .btn{position:absolute;left:86px;top:240px;width:231px;height:62px;background:var(--orange);font-size:21px;font-weight:400}

/* footer */
.footer-nav{position:absolute;left:0;top:2515px;width:1200px;height:62px;background:var(--footer-nav);color:var(--white)}
.footer-links{position:absolute;left:88px;top:23px;display:flex;gap:14px;font-size:11.5px}
.social{position:absolute;right:86px;top:20px;display:flex;gap:8px}
.social i{width:19px;height:19px;background:#fff;border-radius:3px;display:block}
.site-footer{position:absolute;left:0;top:2577px;width:1200px;height:180px;background:var(--footer);color:var(--white)}
.branch{position:absolute;top:45px;font-size:11.5px}
.branch h3{font-size:17px;font-weight:400;margin-bottom:10px}
.branch p{display:flex;align-items:center;gap:12px;margin-left:2px;line-height:24px}
.copyright{position:absolute;left:0;top:2757px;width:1200px;height:38px;background:#1e1e1e;color:#ddd;font-size:11.5px;text-align:center;line-height:38px}
</style>
</head>
<body>

<header class="site-header">
  <div class="brand"><span class="brand-name">Mariners &amp; Bakers</span></div>
  <nav class="utility-nav">
    <a>Home</a><a>Apply For A Loan</a><a>Become A Member</a><a>Locations</a>
    <span class="tel"><svg width="12" height="12" viewBox="0 0 24 24"><path fill="#f37122" d="M6.6 10.8a15 15 0 0 0 6.6 6.6l2.2-2.2c.3-.3.7-.4 1-.2 1.1.4 2.3.6 3.6.6.6 0 1 .4 1 1V20c0 .6-.4 1-1 1A17 17 0 0 1 3 4c0-.6.4-1 1-1h3.5c.6 0 1 .4 1 1 0 1.3.2 2.5.6 3.6.1.3 0 .7-.2 1z"/></svg>(555) 610-4400</span>
    <span class="tel"><svg width="13" height="12" viewBox="0 0 24 22"><rect x="2" y="7" width="20" height="13" fill="#f37122"/><rect x="6" y="2" width="12" height="6" fill="none" stroke="#f37122" stroke-width="2"/></svg>(555) 610-4471</span>
  </nav>
  <nav class="main-nav"><a>My Credit Union</a><a>Products and Services</a><a>Tools and Benefits</a></nav>
  <a class="login-btn">Internet Teller Login <svg width="9" height="6" viewBox="0 0 9 6"><path d="M1 1l3.5 3.5L8 1" stroke="#fff" fill="none" stroke-width="1.5"/></svg></a>
</header>

<section class="hero">
  <div class="hero-photo" role="img" aria-label="Photo of a smiling family playing together on a sunny beach"></div>
  <h1 class="hero-title">Teacher Trainee Loans</h1>
  <p class="hero-copy">All applicants are required to make a 5% equity injection into their projects. No! Shares can NOT count toward qualification. Take this out because fresh funds are now required for this purpose.</p>
  <a class="btn btn-purple">Apply Now</a>
  <div class="dots"><i></i><i class="on"></i><i></i></div>
</section>

<h2 class="section-title" style="top:645px">What are you looking for MBFC?</h2>

<div class="service" style="left:94px">
  <div class="ring"><svg width="60" height="60" viewBox="0 0 60 60" fill="#f37122"><path d="M10 20a20 12 0 0 1 36 0z"/><rect x="27" y="18" width="2.5" height="28"/><rect x="10" y="46" width="40" height="3"/><path d="M22 44l6-10h14l4 10z"/></svg></div>Vacation<br>Club</div>
<div class="service" style="left:291px">
  <div class="ring"><svg width="60" height="60" viewBox="0 0 60 60" fill="#f37122"><rect x="22" y="8" width="18" height="24" rx="2"/><rect x="32" y="14" width="16" height="20" rx="2" opacity=".8"/><path d="M10 46c6-14 14-16 22-14l10 4-4 6-10-2 12 6v6H14z"/></svg></div>Consumer<br>Loans</div>
<div class="service" style="left:489px">
  <div class="ring active"><svg width="64" height="64" viewBox="0 0 64 64" fill="#fff"><path d="M10 30L32 10l22 20h-6v20H16V30z"/><circle cx="40" cy="40" r="8" fill="#f37122"/><circle cx="40" cy="40" r="5" fill="#fff"/><rect x="45" y="45" width="10" height="3" transform="rotate(45 45 45)"/></svg></div>Mortgages</div>
<div class="service" style="left:686px">
  <div class="ring"><svg width="60" height="60" viewBox="0 0 60 60" fill="#f37122"><rect x="14" y="8" width="30" height="42" rx="2"/><circle cx="26" cy="24" r="5" fill="#efe3e3"/><rect x="34" y="34" width="12" height="10" rx="1" fill="#fff" stroke="#f37122" stroke-width="2"/></svg></div>Saftey Deposit<br>Boxes</div>
<div class="service" style="left:884px">
  <div class="ring"><svg width="60" height="60" viewBox="0 0 60 60" fill="#f37122"><circle cx="26" cy="20" r="9"/><path d="M10 48c0-12 8-18 16-18s12 3 14 6v12z"/><circle cx="42" cy="42" r="9"/><circle cx="42" cy="42" r="5" fill="#efe3e3"/></svg></div>Salary<br>Deduction</div>

<section class="rates">
  <h2 class="section-title">Featured Rates</h2>
  <div class="rate-card" style="left:136px">
    <svg width="48" height="56" viewBox="0 0 48 56" fill="#fff"><path d="M16 4h16l-5 8h-6z"/><path d="M19 14h10c10 8 15 18 15 26 0 10-8 14-20 14S4 50 4 40c0-8 5-18 15-26z"/><text x="24" y="46" font-size="20" font-weight="700" text-anchor="middle" fill="#000" font-family="Lato,sans-serif">$</text></svg>
    <div class="rate-name">Consumer Loans</div><div class="rate-sub">as low as</div><div class="rate-value">9.00% APR*</div>
  </div>
  <div class="rate-card" style="left:378px">
    <svg width="120" height="56" viewBox="0 0 120 56" fill="none" stroke="#fff" stroke-width="4"><circle cx="22" cy="38" r="14"/><circle cx="98" cy="38" r="14"/><path d="M22 38l20-18h30l8-8h10l8 26M42 20l14 18h22"/><path d="M46 16h22" stroke-width="8"/></svg>
    <div class="rate-name">New Auto/Motorcycle</div><div class="rate-sub">as low as</div><div class="rate-value">7.00% APR*</div>
  </div>
  <div class="rate-card" style="left:620px">
    <svg width="120" height="56" viewBox="0 0 120 56" fill="#fff"><path d="M8 40V28l12-4 14-16h46l18 16 14 4v12z"/><path d="M38 12h18v12H28zM60 12h18l10 12H60z" fill="#000"/><circle cx="30" cy="42" r="9" fill="#000"/><circle cx="30" cy="42" r="6"/><circle cx="90" cy="42" r="9" fill="#000"/><circle cx="90" cy="42" r="6"/></svg>
    <div class="rate-name">Used Auto/Motorcycle</div><div class="rate-sub">as low as</div><div class="rate-value">11.75% APR*</div>
  </div>
  <div class="rate-card" style="left:863px">
    <svg width="64" height="56" viewBox="0 0 64 56" fill="none" stroke="#fff" stroke-width="5"><path d="M6 26L28 6l22 20M12 22v28h22"/><text x="44" y="50" font-size="34" font-weight="900" fill="#fff" stroke="none" text-anchor="middle" font-family="Lato,sans-serif">$</text></svg>
    <div class="rate-name">Mortgages</div><div class="rate-sub">as low as</div><div class="rate-value">8.25% APR*</div>
  </div>
  <div class="rates-note"><span>*APR - Annual Percentage Rate.</span><a class="btn btn-purple">Apply For A Loan &gt;</a></div>
</section>

<h2 class="section-title" style="top:1530px">News &amp; Events</h2>

<article class="news-card" style="left:86px">
  <div class="news-photo" role="img" aria-label="Photo of a woman in a yellow jacket using an ATM" style="background:linear-gradient(135deg,#c7cbd0,#b9a55a 55%,#8c9aa6)"></div>
  <div class="news-body"><h3 class="news-title">The standard Lorem Ipsum passage</h3>
  <p class="news-text">Lorem ipsum dolor sit amet, consectetur adipiscing elit, sed do eiusmod tempor incididunt ut labore et dolore magna aliqua. Ut enim ad minim veniam</p>
  <div class="news-meta"><span>&#128197; March 07, 2017</span><span>&#128488; 45</span></div></div>
</article>
<article class="news-card" style="left:434px">
  <div class="news-photo" role="img" aria-label="Photo of a woman sitting cross-legged with a laptop" style="background:linear-gradient(180deg,#e4e4e4,#d6d2cc 45%,#c79b3c 60%,#5c7495 85%,#e0e0e0)"></div>
  <div class="news-body"><h3 class="news-title">The standard Lorem Ipsum passage</h3>
  <p class="news-text">Lorem ipsum dolor sit amet, consectetur adipiscing elit, sed do eiusmod tempor incididunt ut labore et dolore magna aliqua. Ut enim ad minim veniam</p>
  <div class="news-meta"><span>&#128197; March 07, 2017</span><span>&#128488; 45</span></div></div>
</article>
<article class="news-card" style="left:782px">
  <div class="news-photo" role="img" aria-label="Photo of a family of four sitting together on a sofa at home" style="background:linear-gradient(160deg,#8f8b86,#cfc8c0 50%,#6f7480)"></div>
  <div class="news-body"><h3 class="news-title">The standard Lorem Ipsum passage</h3>
  <p class="news-text">Lorem ipsum dolor sit amet, consectetur adipiscing elit, sed do eiusmod tempor incididunt ut labore et dolore magna aliqua. Ut enim ad minim veniam</p>
  <div class="news-meta"><span>&#128197; March 07, 2017</span><span>&#128488; 45</span></div></div>
</article>

<section class="notice" role="img" aria-label="Background photo of a smiling woman at an ATM">
  <h2 class="notice-title">ATM CARD RENEWAL NOTICE</h2>
  <p class="notice-copy">Pleace be advised that all ATM Cards issued February 2014,<br><strong>EXPIRES EFFECTIVE FEBRUARY 20. 2017.</strong></p>
  <a class="btn">LEARN MORE</a>
</section>

<nav class="footer-nav">
  <div class="footer-links"><a>Home</a><a>Apply For A Loan</a><a>Become A Member</a><a>Locations</a><a>Privacy Policy</a><a>Website Terms</a><a>USA Patriot Act</a></div>
  <div class="social"><i></i><i></i><i></i><i></i></div>
</nav>

<footer class="site-footer">
  <div class="branch" style="left:167px"><h3>Harborview</h3>
    <p><svg width="9" height="12" viewBox="0 0 9 12"><path fill="#fff" d="M4.5 0A4.5 4.5 0 0 0 0 4.5C0 8 4.5 12 4.5 12S9 8 9 4.5A4.5 4.5 0 0 0 4.5 0zm0 6.3a1.8 1.8 0 1 1 0-3.6 1.8 1.8 0 0 1 0 3.6z"/></svg>Quay Street &amp; Lantern Rd.</p>
    <p><svg width="10" height="10" viewBox="0 0 24 24"><path fill="#fff" d="M6.6 10.8a15 15 0 0 0 6.6 6.6l2.2-2.2c.3-.3.7-.4 1-.2 1.1.4 2.3.6 3.6.6.6 0 1 .4 1 1V20c0 .6-.4 1-1 1A17 17 0 0 1 3 4c0-.6.4-1 1-1h3.5c.6 0 1 .4 1 1 0 1.3.2 2.5.6 3.6.1.3 0 .7-.2 1z"/></svg>(555) 610-4400</p>
    <p><svg width="10" height="10" viewBox="0 0 24 22"><rect x="2" y="7" width="20" height="13" fill="#fff"/><rect x="6" y="2" width="12" height="6" fill="none" stroke="#fff" stroke-width="2"/></svg>(555) 610-4471</p>
  </div>
  <div class="branch" style="left:501px"><h3>Port Sable, Grand Isle</h3>
    <p><svg width="9" height="12" viewBox="0 0 9 12"><path fill="#fff" d="M4.5 0A4.5 4.5 0 0 0 0 4.5C0 8 4.5 12 4.5 12S9 8 9 4.5A4.5 4.5 0 0 0 4.5 0zm0 6.3a1.8 1.8 0 1 1 0-3.6 1.8 1.8 0 0 1 0 3.6z"/></svg>#12 Mill Harbour Dr.</p>
    <p><svg width="10" height="10" viewBox="0 0 24 24"><path fill="#fff" d="M6.6 10.8a15 15 0 0 0 6.6 6.6l2.2-2.2c.3-.3.7-.4 1-.2 1.1.4 2.3.6 3.6.6.6 0 1 .4 1 1V20c0 .6-.4 1-1 1A17 17 0 0 1 3 4c0-.6.4-1 1-1h3.5c.6 0 1 .4 1 1 0 1.3.2 2.5.6 3.6.1.3 0 .7-.2 1z"/></svg>(555) 720-3318</p>
    <p><svg width="10" height="10" viewBox="0 0 24 22"><rect x="2" y="7" width="20" height="13" fill="#fff"/><rect x="6" y="2" width="12" height="6" fill="none" stroke="#fff" stroke-width="2"/></svg>(555) 720-3390</p>
  </div>
  <div class="branch" style="left:832px"><h3>Coral Cay</h3>
    <p><svg width="9" height="12" viewBox="0 0 9 12"><path fill="#fff" d="M4.5 0A4.5 4.5 0 0 0 0 4.5C0 8 4.5 12 4.5 12S9 8 9 4.5A4.5 4.5 0 0 0 4.5 0zm0 6.3a1.8 1.8 0 1 1 0-3.6 1.8 1.8 0 0 1 0 3.6z"/></svg>Saltmarsh Market Plaza</p>
    <p><svg width="10" height="10" viewBox="0 0 24 24"><path fill="#fff" d="M6.6 10.8a15 15 0 0 0 6.6 6.6l2.2-2.2c.3-.3.7-.4 1-.2 1.1.4 2.3.6 3.6.6.6 0 1 .4 1 1V20c0 .6-.4 1-1 1A17 17 0 0 1 3 4c0-.6.4-1 1-1h3.5c.6 0 1 .4 1 1 0 1.3.2 2.5.6 3.6.1.3 0 .7-.2 1z"/></svg>(555) 830-2256</p>
    <p><svg width="10" height="10" viewBox="0 0 24 22"><rect x="2" y="7" width="20" height="13" fill="#fff"/><rect x="6" y="2" width="12" height="6" fill="none" stroke="#fff" stroke-width="2"/></svg>(555) 830-2257</p>
  </div>
</footer>

<div class="copyright">Copyright © 2017 Mariners &amp; Bakers Regional Co-operative Credit Union Ltd. All Rights Reserved.</div>

</body>
</html>
```